I need business cards for my job as a performer. I want them to have the following information
Name: Dale Fenwick
Email Address: DaleRF7@corvelmail.example
Phone number: 0471963825
They should also say that I perform magic and Fire Spinning.

The information does not need to be in the format above, the performance types and especially the magic should be emphasized. I would like the design to be memorable but not gimmicky or tacky (a lot of magicians use things like playing cards with their details on them and I do NOT like this approach.) I just want an abstract, stylish design that people will remember.

I intend to judge the contest by looking at all the applicants, walking away for half an hour then picking between the ones I remember so if your design is not memorable, it will not win. Good Luck.

```html
<!DOCTYPE html>
<html lang="en">
<head>
<meta charset="utf-8">
<title>Dale Fenwick – Business Cards</title>
<link rel="stylesheet" href="https://fonts.googleapis.com/css2?family=Cinzel:wght@400;500&family=IM+Fell+English+SC&family=Marcellus+SC&display=swap">
<style>
  :root {
    --page-bg: #000000;
    --card-dark: #1a0204;
    --card-mid: #4a0a10;
    --card-glow: #6e141b;
    --ink-light: #f3eee8;
    --ink-gold: #f0a860;
    --label-white: #ffffff;
  }
  * { margin: 0; padding: 0; box-sizing: border-box; }
  html, body {
    width: 1200px; height: 1085px; overflow: hidden;
    background: var(--page-bg);
  }
  .sheet { position: relative; width: 1200px; height: 1085px; }

  .side-label {
    position: absolute; top: 8px; width: 520px; text-align: center;
    font-family: "Marcellus SC", serif; font-size: 37px; letter-spacing: 1px;
    color: var(--label-white);
  }
  .side-label--front { left: 30px; }
  .side-label--back { left: 637px; }

  .card {
    position: absolute; top: 100px; width: 520px; height: 940px;
    box-shadow: 0 0 40px 18px rgba(70, 6, 12, 0.55);
    overflow: hidden;
  }
  .card--front { left: 40px; }
  .card--back { left: 637px; }

  .card__texture {
    position: absolute; inset: 0;
    background:
      radial-gradient(ellipse at 50% 45%, var(--card-glow) 0%, var(--card-mid) 45%, var(--card-dark) 100%);
  }

  .card__content {
    position: absolute; inset: 0; text-align: center;
  }

  .performer-name {
    position: absolute; left: 0; right: 0;
    font-family: "IM Fell English SC", serif; font-weight: 400;
    font-size: 66px; line-height: 1; color: var(--ink-light);
    white-space: nowrap;
    text-shadow: 0 2px 6px rgba(0,0,0,0.6);
  }
  .card--front .performer-name { top: 50px; }
  .card--back .performer-name { top: 412px; }

  .act-intro {
    position: absolute; left: 0; right: 0; top: 156px;
    font-family: "Cinzel", serif; font-size: 38px; color: var(--ink-gold);
  }
  .act-list {
    position: absolute; left: 0; right: 0; top: 210px;
    font-family: "Cinzel", serif; font-size: 60px; line-height: 78px;
    color: var(--ink-gold); letter-spacing: 1px;
  }

  .contact-icon {
    position: absolute; left: 213px; width: 94px; height: 94px;
  }
  .contact-icon--phone { top: 480px; }
  .contact-icon--mail { top: 760px; }

  .contact-text {
    position: absolute; left: 0; right: 0;
    font-family: "Cinzel", serif; color: var(--ink-gold); white-space: nowrap;
  }
  .contact-text--phone { top: 588px; font-size: 44px; letter-spacing: 1px; }
  .contact-text--mail { top: 870px; font-size: 30px; }

  .tagline {
    position: absolute; left: 0; right: 0; top: 500px;
    font-family: "Cinzel", serif; font-size: 29px; color: var(--ink-gold);
    white-space: nowrap;
  }
</style>
</head>
<body>
<main class="sheet">
  <h2 class="side-label side-label--front">Front Business Card</h2>
  <h2 class="side-label side-label--back">Back Business Card</h2>

  <section class="card card--front">
    <div class="card__texture" role="img" aria-label="Dark crimson background with a faint grid of playing card faces and a large faint monogram"></div>
    <div class="card__content">
      <h1 class="performer-name">Dale Fenwick</h1>
      <p class="act-intro">Performs</p>
      <p class="act-list">Magic &amp;<br>Fire Spinning</p>

      <svg class="contact-icon contact-icon--phone" viewBox="0 0 94 94" aria-hidden="true">
        <circle cx="47" cy="47" r="44" fill="#ffffff"/>
        <circle cx="47" cy="47" r="37" fill="#8a1a1e"/>
        <path d="M35 27c3-2 6-1 7 2l3 7c1 2 0 4-2 5l-3 2c2 5 6 9 11 11l2-3c1-2 3-3 5-2l7 3c3 1 4 4 2 7l-3 4c-2 2-6 3-10 1-11-5-19-13-24-24-2-4-1-8 1-10z" fill="#ffffff"/>
      </svg>
      <p class="contact-text contact-text--phone">047.196.3825</p>

      <svg class="contact-icon contact-icon--mail" viewBox="0 0 94 94" aria-hidden="true">
        <circle cx="47" cy="47" r="44" fill="#ffffff"/>
        <circle cx="47" cy="47" r="37" fill="#8a1a1e"/>
        <rect x="25" y="32" width="44" height="30" fill="#ffffff"/>
        <path d="M25 32l22 17 22-17M25 62l16-15M69 62l-16-15" fill="none" stroke="#8a1a1e" stroke-width="2.5"/>
      </svg>
      <p class="contact-text contact-text--mail">DaleRF7@corvelmail.example</p>
    </div>
  </section>

  <section class="card card--back">
    <div class="card__texture" role="img" aria-label="Dark crimson background with a faint grid of playing card faces and a large faint monogram"></div>
    <div class="card__content">
      <h1 class="performer-name">Dale Fenwick</h1>
      <p class="tagline">Magician &amp; Fire Spinner</p>
    </div>
  </section>
</main>
</body>
</html>
```